Mosque App design fresh look and feel

Need to create a mosque app which has half a couple of dozen pages, a login page will take you into the main information with about 6 categories, such as school, memberships, information, prayer times etc... we have 3 types of users... 1. User .. admin user 3. imam user

I have xd files available.
https://mockview.plorvent.com/view/e81f27da-5c04-4b9e-91a3-7fd20b6c4a85-3c1d/

Target Market(s)

Muslims

Font styles to use
Sans Serif

Requirements
Must have
• Great UI
Simple flow

```html
<!DOCTYPE html>
<html lang="en">
<head>
<meta charset="utf-8">
<title>Our Darsora – Login</title>
<link rel="stylesheet" href="https://fonts.googleapis.com/css2?family=Cormorant+SC:wght@600&family=Open+Sans:wght@400;700&display=swap">
<style>
  :root {
    --gold: #c2955e;
    --gold-deep: #9c7240;
    --bg-top: #0a0b0e;
    --bg-mid: #1a1c24;
    --bg-bottom: #2c2f3d;
    --field: #ffffff;
    --placeholder: #9a9a9a;
    --text-light: #ffffff;
  }
  * { box-sizing: border-box; margin: 0; padding: 0; }
  html, body { width: 1200px; height: 2598px; overflow: hidden; }
  body {
    position: relative;
    background: linear-gradient(165deg, var(--bg-top) 0%, var(--bg-mid) 45%, var(--bg-bottom) 100%);
    font-family: "Open Sans", sans-serif;
    color: var(--text-light);
  }
  .status-bar { position: absolute; top: 0; left: 0; width: 1200px; height: 140px; }
  .status-time {
    position: absolute; left: 66px; top: 41px; width: 172px; height: 66px;
    border-radius: 33px; background: var(--gold);
    font: 700 46px/66px "Open Sans", sans-serif; text-align: center; color: #fff;
  }
  .status-icons { position: absolute; right: 44px; top: 52px; }
  .brand {
    position: absolute; top: 0; left: 0; width: 1200px; height: 0;
    font-family: "Cormorant SC", serif; font-weight: 600; color: var(--gold);
    text-transform: uppercase;
  }
  .brand-line {
    position: absolute; left: 0; width: 1200px; text-align: center;
    font-size: 132px; line-height: 132px; letter-spacing: 2px;
  }
  .brand-line-top { top: 508px; }
  .brand-line-main { top: 633px; }
  .brand-rule {
    position: absolute; left: 497px; top: 778px; width: 206px; height: 6px; background: var(--gold);
  }
  .login-form { position: absolute; left: 198px; top: 898px; width: 829px; }
  .field {
    display: block; background: var(--field); border: none; border-radius: 8px;
    height: 132px; padding-left: 56px;
    font: 400 43px "Open Sans", sans-serif; color: #333;
  }
  .field::placeholder { color: var(--placeholder); }
  .field-email { width: 829px; }
  .form-row { display: flex; justify-content: space-between; margin-top: 52px; }
  .field-password { width: 489px; }
  .login-button {
    width: 296px; height: 132px; border: none; border-radius: 8px; background: var(--gold);
    font: 700 43px "Open Sans", sans-serif; color: #fff; letter-spacing: 1px;
  }
  .jamat-card {
    position: absolute; left: 198px; top: 1411px; width: 829px; height: 429px;
    border: 2px solid var(--gold); border-radius: 30px; text-align: center;
  }
  .jamat-title { margin-top: 46px; font-size: 41px; line-height: 56px; font-weight: 700; letter-spacing: -0.5px; }
  .jamat-list { list-style: none; margin-top: 20px; }
  .jamat-list li { font-size: 43px; line-height: 63px; }
  .ornament { position: absolute; left: 0; top: 1975px; width: 1200px; height: 623px; }
</style>
</head>
<body>
  <div class="status-bar">
    <div class="status-time">9:41</div>
    <svg class="status-icons" width="220" height="44" viewBox="0 0 220 44" aria-hidden="true">
      <g fill="#fff">
        <rect x="0" y="26" width="10" height="12" rx="2"/>
        <rect x="15" y="19" width="10" height="19" rx="2"/>
        <rect x="30" y="12" width="10" height="26" rx="2"/>
        <rect x="45" y="4" width="10" height="34" rx="2"/>
        <path d="M96 38 l-9 -10 a13 13 0 0 1 18 0z"/>
        <path d="M80 20 a23 23 0 0 1 32 0 l-5 5 a16 16 0 0 0 -22 0z"/>
        <path d="M73 12 a33 33 0 0 1 46 0 l-4 5 a27 27 0 0 0 -38 0z"/>
        <rect x="139" y="4" width="70" height="34" rx="9" fill="none" stroke="#fff" stroke-width="3" opacity="0.5"/>
        <rect x="143" y="8" width="62" height="26" rx="6"/>
        <rect x="212" y="16" width="4" height="11" rx="2" opacity="0.5"/>
      </g>
    </svg>
  </div>

  <h1 class="brand">
    <span class="brand-line brand-line-top">Our</span>
    <span class="brand-line brand-line-main">Darsora</span>
  </h1>
  <div class="brand-rule"></div>

  <form class="login-form">
    <input class="field field-email" type="email" placeholder="Email Address">
    <div class="form-row">
      <input class="field field-password" type="password" placeholder="Password">
      <button class="login-button" type="button">LOGIN</button>
    </div>
  </form>

  <section class="jamat-card">
    <h2 class="jamat-title">JAMAT TIMES</h2>
    <ul class="jamat-list">
      <li>Dummy Time - 3:00 PM - 8:00 PM</li>
      <li>Dummy Time - 3:00 PM - 8:00 PM</li>
      <li>Dummy Time - 3:00 PM - 8:00 PM</li>
      <li>Dummy Time - 3:00 PM - 8:00 PM</li>
    </ul>
  </section>

  <svg class="ornament" viewBox="0 0 1200 623" role="img" aria-label="Gold mandala ornament rising from the bottom edge">
    <defs>
      <radialGradient id="mandalaTone" cx="600" cy="760" r="760" gradientUnits="userSpaceOnUse">
        <stop offset="0" stop-color="#c2955e" stop-opacity="0.55"/>
        <stop offset="0.7" stop-color="#9c7240" stop-opacity="0.35"/>
        <stop offset="1" stop-color="#9c7240" stop-opacity="0.15"/>
      </radialGradient>
    </defs>
    <circle cx="600" cy="760" r="760" fill="url(#mandalaTone)"/>
  </svg>
</body>
</html>
```